Business card for utility of the future

I need a business card template designed for brookvane. We provide sustainable water, energy and waste services to homes.

The card should include name, position, email address, phone number, website and our logo (attached). I would like it to convey professionalism and creativity.

Target Market(s)

Homeowners, investors, corporate partners.

Industry/Entity Type

Utility

Contact Information for Business Card

The card should include name, position, email address, phone number, website and our logo (attached).

```html
<!DOCTYPE html>
<html lang="en">
<head>
<meta charset="utf-8">
<title>brookvane business card</title>
<link rel="stylesheet" href="https://fonts.googleapis.com/css2?family=Arimo:wght@400;700&display=swap">
<style>
  :root {
    --backdrop: #2a2a2a;
    --card-light: #ffffff;
    --card-shade: #ebebeb;
    --brand-green: #4f9e6b;
    --band-green: #5aa775;
    --tint-green: #eef6f0;
    --ink: #222222;
    --ink-soft: #444444;
  }
  * { margin: 0; padding: 0; box-sizing: border-box; }
  html, body {
    width: 1200px; height: 997px; overflow: hidden;
    background: var(--backdrop);
    font-family: "Arimo", Arial, sans-serif;
  }
  .stage {
    position: relative; width: 1200px; height: 997px;
    display: flex; flex-direction: column; align-items: center; justify-content: center; gap: 34px;
  }
  .card {
    position: relative; width: 760px; height: 434px;
    border-radius: 22px; overflow: hidden;
    background: linear-gradient(160deg, var(--card-light) 0%, var(--card-shade) 100%);
    box-shadow: 0 10px 30px rgba(0,0,0,.45);
  }

  /* front */
  .front {
    background: linear-gradient(160deg, var(--card-light) 0%, var(--tint-green) 55%, var(--card-shade) 100%);
  }
  .brand-name {
    color: var(--brand-green); font-weight: 700; letter-spacing: -1px;
    white-space: nowrap; line-height: 1;
  }
  .front .brand-name {
    position: absolute; left: 50%; top: 50%; transform: translate(-50%, -50%);
    font-size: 100px;
  }

  /* back */
  .back .brand-name {
    position: absolute; left: 64px; top: 180px; font-size: 56px;
  }
  .divider {
    position: absolute; left: 402px; top: 60px; width: 3px; height: 250px;
    background: linear-gradient(180deg, transparent, var(--brand-green) 40%, var(--brand-green) 60%, transparent);
  }
  .contact { position: absolute; left: 440px; top: 76px; }
  .contact .name { color: var(--brand-green); font-weight: 700; font-size: 20px; }
  .contact .role { color: var(--ink); font-size: 15px; margin-top: 4px; }
  .contact ul { list-style: none; margin-top: 26px; }
  .contact li {
    display: flex; align-items: center; gap: 14px;
    color: var(--ink-soft); font-size: 18px; margin-bottom: 16px;
  }
  .contact svg { width: 16px; height: 16px; fill: var(--ink-soft); flex: none; }
  .band {
    position: absolute; left: 0; right: 0; bottom: 0; height: 86px;
    background: var(--band-green);
    display: flex; align-items: center; justify-content: center;
    color: #ffffff; font-weight: 700; font-size: 20px; letter-spacing: 6px;
  }
</style>
</head>
<body>
<main class="stage">
  <section class="card front" aria-label="Card front">
    <p class="brand-name">brookvane</p>
  </section>

  <section class="card back" aria-label="Card back">
    <p class="brand-name">brookvane</p>
    <div class="divider"></div>
    <div class="contact">
      <p class="name">Daniel Ashcombe</p>
      <p class="role">Chairman</p>
      <ul>
        <li>
          <svg viewBox="0 0 16 16" aria-hidden="true"><path d="M3 1h3l1.5 3.5-2 1.3a9 9 0 0 0 4.7 4.7l1.3-2L15 10v3a2 2 0 0 1-2 2A12 12 0 0 1 1 3a2 2 0 0 1 2-2z"/></svg>
          0402718354
        </li>
        <li>
          <svg viewBox="0 0 16 16" aria-hidden="true"><path d="M1 3h14v10H1z M2 4l6 5 6-5" fill="none" stroke="#444" stroke-width="1.6"/></svg>
          da@brookvane.com
        </li>
        <li>
          <svg viewBox="0 0 16 16" aria-hidden="true"><path d="M8 0a5.5 5.5 0 0 0-5.5 5.5C2.5 10 8 16 8 16s5.5-6 5.5-10.5A5.5 5.5 0 0 0 8 0zm0 8a2.5 2.5 0 1 1 0-5 2.5 2.5 0 0 1 0 5z"/></svg>
          14 Fernhill Rd, Lakeview
        </li>
      </ul>
    </div>
    <div class="band">www.brookvane.com</div>
  </section>
</main>
</body>
</html>
```